New solo practice law firm is looking for an elegant, professional, and interactive web design

I need a web design and developer for a new small law firm in Sacramento, California called Dorian Kessly Law, A Professional Corporation. I am a trial lawyer who represents average people facing difficult litigation disputes, including criminal defense as a former prosecutor and civil litigation as a civil litigator. Criminal defense includes domestic violence, battery, assault, drug possession, theft, DUI, etc. Civil litigation includes business disputes, property disputes, employment disputes, family law disputes, and immigration issues. I would like to see web designs that incorporate my logo and use the logo's navy blue and gold colors. I have uploaded the files of my logo to this brief. Please only use the navy blue and gold version. Overall, I want the design to look firm, professional, and elegant.

I plan on having the following pages on my website: (1) Home, (2) Dorian Kessly, (3) Practice Areas, (4) Insights, (5) Contact. I've hand drawn a preliminary sketch concept of what I envision the home page's layout to look like (attached with a text version). I would like your design to keep a similar layout for the homepage and incorporate my logo's colors within it but I am open to creative layout alternatives/ideas. I would like the other pages to have a similar look and feel as the home page. Some of the areas currently in my sketch do not have the full text. You can insert other text for now and I will provide the winner the full text.

In terms of the pictures on the website, I enjoy images of courthouses, columns (example attached but I cannot use this one), and, if possible, images from Sacramento, CA in my background (headshot attached). A plus would be live images that move and also sections of the webpage moving in the viewers view as they scroll down on the page. Also, it would be great to have my logo act as the tab for the website. I can provide other versions of the logo if needed.

I look forward to seeing your Wordpress designs!

People needing legal representation.

Law

Coded - Design and coding required

5+ page

Serif

• Incorporate my logo and my logo's colors.
• Live pictures and images appearing as viewers scroll on page.

```html
<!DOCTYPE html>
<html lang="en">
<head>
<meta charset="utf-8">
<title>Dorian Kessly Law</title>
<link href="https://fonts.googleapis.com/css2?family=Urbanist:wght@400;500;600;700;800&display=swap" rel="stylesheet">
<style>
:root{
  --navy:#13223b;
  --navy-soft:#33465f;
  --gold:#ab9263;
  --gold-deep:#a38a5c;
  --dark:#23272c;
  --darker:#1e2227;
  --ink:#1f1f1f;
  --text:#444;
  --white:#fff;
  --blue-frame:#1d58a6;
  --orange:#f07d16;
}
*{margin:0;padding:0;box-sizing:border-box}
html,body{width:1200px;height:2795px;overflow:hidden;background:var(--white)}
body{font-family:"Urbanist",sans-serif;color:var(--ink);position:relative}
.abs{position:absolute}
a{color:inherit;text-decoration:none}
.pill{background:var(--gold);color:var(--white);border-radius:22px;display:flex;align-items:center;justify-content:center;font-weight:600;text-transform:uppercase}

/* header */
.header{top:0;left:0;width:1200px;height:98px}
.brand{left:150px;top:14px;width:125px;display:flex;flex-direction:column;align-items:center;gap:8px}
.brand-mark{width:40px;height:40px;border:2px solid var(--navy)}
.brand-name{font-size:9px;font-weight:600;letter-spacing:1.5px;color:var(--navy);text-align:center;line-height:1.3}
.topline{top:14px;right:0;width:520px;height:42px}
.phone{left:5px;top:8px;display:flex;align-items:center;gap:10px;font-size:13px;font-weight:700}
.quote-btn{left:206px;top:0;width:110px;height:30px;font-size:11px}
.nav{left:372px;top:56px;width:828px;height:42px;background:var(--navy);clip-path:polygon(22px 0,100% 0,100% 100%,0 100%)}
.nav ul{list-style:none;display:flex;position:absolute;left:53px;top:0;height:42px;align-items:center}
.nav li{color:var(--white);font-size:12.5px;font-weight:500;margin-right:60px;position:relative}
.nav li.active::after{content:"";position:absolute;left:0;right:0;bottom:-14px;height:2px;background:var(--gold)}

/* hero */
.hero{top:98px;left:0;width:1200px;height:600px;background:linear-gradient(90deg,#2a2721 0%,#4d4231 35%,#2b251d 60%,#3b3124 85%,#1a1713 100%)}
.hero h1{left:162px;top:215px;color:var(--white);font-size:40px;font-weight:800;line-height:50px;text-transform:uppercase}
.hero .cta{left:163px;top:347px;width:166px;height:36px;font-size:13px}
.arrow-circle{width:48px;height:48px;border:2px solid var(--white);border-radius:50%;display:flex;align-items:center;justify-content:center}

/* about */
.about-photo{left:210px;top:805px;width:312px;height:361px;background:linear-gradient(180deg,#b09863,#9d8658);border-radius:2px}
.about-label{left:580px;top:822px;font-size:16px;font-weight:700;color:var(--navy);display:flex;align-items:center;gap:10px}
.about-label::before{content:"";width:26px;height:2px;background:var(--gold)}
.about-title{left:580px;top:856px;font-size:21px;font-weight:700;color:var(--navy)}
.about-lead{left:580px;top:893px;width:405px;font-size:14px;line-height:23px;color:#333;font-weight:500}
.about-body{left:580px;top:975px;width:395px;font-size:12.5px;line-height:24px;color:var(--text)}
.about-btn{left:580px;top:1097px;width:138px;height:38px;font-size:13px}

/* services */
.svc-head{left:434px;top:1281px;width:332px;height:58px;border:3px solid var(--blue-frame)}
.svc-kicker{left:50%;top:-17px;transform:translateX(-50%);background:var(--white);padding:0 10px;color:var(--orange);font-size:18px;font-weight:600;white-space:nowrap}
.svc-title{left:0;right:0;top:10px;text-align:center;font-size:33px;font-weight:800;color:var(--ink)}
.svc-bg{left:0;top:1380px;width:1200px;height:555px}
.svc-circle{width:196px;height:196px;border-radius:50%;border:6px solid #a8905f;background:linear-gradient(135deg,#d9d6d0,#6d6a66)}
.svc-card{width:200px;text-align:center;color:var(--white)}
.svc-card h3{font-size:18px;font-weight:700;margin-bottom:9px}
.svc-card p{font-size:12.5px;line-height:18px}
.svc-card .go{width:34px;height:34px;border-radius:50%;background:rgba(255,255,255,.35);margin:12px auto 0;display:flex;align-items:center;justify-content:center}
.svc-all{left:531px;top:1806px;width:138px;height:37px;font-size:13px}

/* quote */
.quote-photo{left:0;top:1935px;width:553px;height:450px;background:linear-gradient(135deg,#dfe4ea,#9eabbb 60%,#5f6b7b)}
.quote-panel{left:553px;top:1935px;width:647px;height:450px;background:linear-gradient(120deg,#a58c5d,#9d8557)}
.q-kicker{left:64px;top:66px;font-size:11px;color:rgba(255,255,255,.3)}
.q-title{left:71px;top:91px;font-size:27px;font-weight:600;color:var(--white)}
.field{border:1px solid rgba(255,255,255,.35);color:var(--white);font-size:11px;padding:10px 12px}
.send{left:67px;top:344px;width:344px;height:34px;background:#000;color:var(--white);font-size:9.5px;font-weight:700;letter-spacing:.6px;display:flex;align-items:center;justify-content:center}

/* cta bar */
.cta-bar{left:0;top:2385px;width:1200px;height:78px;background:var(--dark);border-bottom:1px solid #33383e}
.cta-bar p{left:248px;top:28px;font-size:19px;color:var(--white)}
.cta-bar .btn{left:841px;top:24px;width:138px;height:34px;background:var(--gold);color:var(--white);font-size:10.5px;font-weight:700;display:flex;align-items:center;justify-content:center}

/* footer */
.footer{left:0;top:2463px;width:1200px;height:269px;background:var(--dark);color:#c9c9c9}
.f-brand{left:200px;top:32px;width:130px;display:flex;flex-direction:column;align-items:center;gap:9px}
.f-brand .brand-mark{border-color:var(--white);width:46px;height:46px}
.f-brand .brand-name{color:var(--white)}
.f-about{left:180px;top:150px;width:195px;font-size:10px;line-height:14px}
.f-div{width:1px;background:#3d4248;top:45px;height:182px}
.f-col h4{color:var(--white);font-size:16px;font-weight:500;position:relative;margin-bottom:22px}
.f-col h4::before{content:"";position:absolute;left:0;top:-14px;width:30px;height:2px;background:var(--gold)}
.f-col li{list-style:none;font-size:11.5px;margin-bottom:7px}
.c-row{display:flex;gap:10px;font-size:11.5px;line-height:16px;margin-bottom:14px}
.social{display:flex;gap:6px}
.social span{width:21px;height:21px;border-radius:50%;background:var(--gold)}
.news{display:flex;width:146px;height:28px;margin-top:10px}
.news div:first-child{flex:1;background:var(--white);color:#888;font-size:9px;padding:8px 10px}
.news div:last-child{width:27px;background:var(--gold);display:flex;align-items:center;justify-content:center}
.bottom{left:0;top:2732px;width:1200px;height:63px;background:var(--darker);color:#b8b8b8;font-size:11.5px}
</style>
</head>
<body>

<header class="header abs">
  <div class="brand abs"><span class="brand-mark"></span><span class="brand-name">DORIAN KESSLY LAW<br><span style="font-size:5px;letter-spacing:1px">A PROFESSIONAL CORPORATION</span></span></div>
  <div class="topline abs">
    <div class="phone abs">
      <svg width="24" height="24" viewBox="0 0 24 24"><path d="M5 3l4 1 1 5-2 2c1 3 3 5 6 6l2-2 5 1 1 4c-1 2-3 2-5 2C10 21 3 14 3 8c0-2 0-4 2-5z" fill="none" stroke="#ab9263" stroke-width="1.6"/><path d="M15 3a6 6 0 016 6M14 7a3 3 0 013 3" stroke="#ab9263" fill="none" stroke-width="1.4"/></svg>
      916 555 0142
    </div>
    <a class="quote-btn pill abs">Get a Quote</a>
  </div>
  <nav class="nav abs"><ul>
    <li class="active">HOME</li><li>DORIAN KESSLY</li><li>PRACTICE AREAS</li><li>INSIGHTS</li><li>CONTACT</li>
  </ul></nav>
</header>

<section class="hero abs" role="img" aria-label="Two men in suits standing among stone courthouse columns beside a lamp post">
  <h1 class="abs">Lorem Ipsum is<br>simply dummy text</h1>
  <a class="cta pill abs" style="text-transform:uppercase;font-weight:500">Contact Us Now</a>
  <div class="arrow-circle abs" style="left:41px;top:237px"><svg width="16" height="16" viewBox="0 0 16 16"><path d="M11 2L5 8l6 6" stroke="#fff" stroke-width="2.6" fill="none"/></svg></div>
  <div class="arrow-circle abs" style="left:1109px;top:237px"><svg width="16" height="16" viewBox="0 0 16 16"><path d="M5 2l6 6-6 6" stroke="#fff" stroke-width="2.6" fill="none"/></svg></div>
  <svg class="abs" style="left:588px;top:524px" width="24" height="42" viewBox="0 0 24 42"><rect x="3" y="1" width="18" height="26" rx="9" fill="none" stroke="#fff" stroke-width="1.6"/><line x1="12" y1="6" x2="12" y2="11" stroke="#fff" stroke-width="1.6"/><path d="M12 30v10M8 36l4 4 4-4" stroke="#fff" fill="none" stroke-width="1.4"/></svg>
</section>

<section class="about">
  <div class="about-photo abs" role="img" aria-label="Portrait of the attorney in a dark suit"></div>
  <div class="about-label abs">About Us</div>
  <h2 class="about-title abs">LOREM IPSUM IS SIMPLY DUMMY TEXT</h2>
  <p class="about-lead abs">Lorem Ipsum is simply dummy text of the printing and typesetting industry. Lorem Ipsum has been the industry's standard dummy text ever since the 1500s,</p>
  <p class="about-body abs">Lorem Ipsum is simply dummy text of the printing and typesetting industry. Lorem Ipsum has been the industry's standard dummy text ever since the 1500s,</p>
  <a class="about-btn pill abs" style="font-weight:600">Learn More</a>
</section>

<section class="services">
  <div class="svc-head abs"><span class="svc-kicker abs">OUR SERVICES</span><h2 class="svc-title abs">WHAT WE DO</h2></div>
  <svg class="svc-bg abs" viewBox="0 0 1200 555" preserveAspectRatio="none" role="img" aria-label="Smiling woman working at an office desk behind a navy overlay">
    <defs><linearGradient id="svcg" x1="0" y1="0" x2="1" y2="1"><stop offset="0" stop-color="#2e4060"/><stop offset=".5" stop-color="#4b5870"/><stop offset="1" stop-color="#1e2e48"/></linearGradient></defs>
    <path d="M0 112 Q600 -110 1200 112 V555 H0Z" fill="#c9d0db"/>
    <path d="M0 118 Q600 -100 1200 118 V555 H0Z" fill="url(#svcg)"/>
  </svg>
  <div class="svc-circle abs" style="left:202px;top:1411px" role="img" aria-label="Gavel on legal documents"></div>
  <div class="svc-circle abs" style="left:502px;top:1381px" role="img" aria-label="Lawyer meeting with a couple"></div>
  <div class="svc-circle abs" style="left:794px;top:1411px" role="img" aria-label="Gavel on legal documents"></div>
  <div class="svc-card abs" style="left:200px;top:1657px"><h3>Lorem Ipsum</h3><p>Lorem ipsum dolor sit amet in consectetur adipiscing elit Maur in rhoncus orci pellente.</p><div class="go"><svg width="14" height="14" viewBox="0 0 14 14"><path d="M2 7h10M8 3l4 4-4 4" stroke="#fff" stroke-width="1.6" fill="none"/></svg></div></div>
  <div class="svc-card abs" style="left:500px;top:1627px"><h3>Lorem Ipsum</h3><p>Lorem ipsum dolor sit amet in consectetur adipiscing elit Maur in rhoncus orci pellente.</p><div class="go"><svg width="14" height="14" viewBox="0 0 14 14"><path d="M2 7h10M8 3l4 4-4 4" stroke="#fff" stroke-width="1.6" fill="none"/></svg></div></div>
  <div class="svc-card abs" style="left:792px;top:1657px"><h3>Lorem Ipsum</h3><p>Lorem ipsum dolor sit amet in consectetur adipiscing elit Maur in rhoncus orci pellente.</p><div class="go"><svg width="14" height="14" viewBox="0 0 14 14"><path d="M2 7h10M8 3l4 4-4 4" stroke="#fff" stroke-width="1.6" fill="none"/></svg></div></div>
  <a class="svc-all pill abs">All Services</a>
</section>

<section class="quote">
  <div class="quote-photo abs" role="img" aria-label="Two businessmen reviewing a tablet in a bright office"></div>
  <div class="quote-panel abs">
    <span class="q-kicker abs">Book An Appoinment</span>
    <h2 class="q-title abs">Request A Quote</h2>
    <div class="field abs" style="left:69px;top:157px;width:156px;height:33px">Your Name</div>
    <div class="field abs" style="left:240px;top:157px;width:172px;height:33px">Your Email</div>
    <div class="field abs" style="left:69px;top:204px;width:343px;height:33px">Subject</div>
    <div class="field abs" style="left:69px;top:250px;width:343px;height:83px">Your Message</div>
    <div class="send abs">SEND REQUEST</div>
  </div>
</section>

<div class="cta-bar abs"><p class="abs">Lorem Ipsum is simply dummy text of the printing</p><a class="btn abs">CONTACT US NOW!!</a></div>

<footer class="footer abs">
  <div class="f-brand abs"><span class="brand-mark"></span><span class="brand-name">DORIAN KESSLY LAW<br><span style="font-size:5px;letter-spacing:1px">A PROFESSIONAL CORPORATION</span></span></div>
  <p class="f-about abs">Lorem ipsum dolor sit amet, consectetur adipiscing elit. Nullam sollicitudin tempor sem vitae pretium. Fusce ultricies mollis purus non rutrum.</p>
  <div class="f-div abs" style="left:392px"></div>
  <div class="f-col abs" style="left:446px;top:64px"><h4>Site Links</h4><ul><li>Home</li><li>Dorian Kessly</li><li>Practice Areas</li><li>Insights</li><li>Contact Us</li></ul></div>
  <div class="f-div abs" style="left:560px"></div>
  <div class="f-col abs" style="left:603px;top:64px;width:180px"><h4>Contact Us</h4>
    <div class="c-row"><svg width="15" height="15" viewBox="0 0 24 24"><path d="M5 3l4 1 1 5-2 2c1 3 3 5 6 6l2-2 5 1 1 4c-1 2-3 2-5 2C10 21 3 14 3 8c0-2 0-4 2-5z" fill="none" stroke="#ccc" stroke-width="1.6"/></svg>Phone: 123 555 01987</div>
    <div class="c-row"><svg width="15" height="15" viewBox="0 0 24 24" style="flex:none"><path d="M12 22s-7-7-7-12a7 7 0 0114 0c0 5-7 12-7 12z" fill="none" stroke="#ccc" stroke-width="1.6"/><circle cx="12" cy="10" r="2.5" fill="none" stroke="#ccc" stroke-width="1.6"/></svg>Address: 123 Some State in USA at 12th Street, 23th New York, Ny</div>
    <div class="c-row"><svg width="15" height="15" viewBox="0 0 24 24"><rect x="3" y="6" width="18" height="13" fill="none" stroke="#ccc" stroke-width="1.6"/><path d="M3 6l9 7 9-7" fill="none" stroke="#ccc" stroke-width="1.6"/></svg>Email: mail@kesslylaw-demo.com</div>
  </div>
  <div class="f-div abs" style="left:815px"></div>
  <div class="f-col abs" style="left:871px;top:64px;width:152px"><h4>Get Connected</h4>
    <div class="social" style="margin-top:-8px"><span></span><span></span><span></span></div>
    <div style="height:1px;background:#3d4248;margin:22px 0 32px"></div>
    <h4 style="margin-bottom:8px">Newsletter</h4>
    <div class="news"><div>Email...</div><div><svg width="13" height="13" viewBox="0 0 14 14"><path d="M1 7l12-6-4 12-2-5z" fill="#fff"/></svg></div></div>
  </div>
</footer>
<div class="bottom abs">
  <span class="abs" style="left:189px;top:24px">@2021 Dorian Kessly Law&nbsp; | &nbsp;All Rights Reserved.</span>
  <span class="abs" style="left:824px;top:24px">Terms &amp; Conditions&nbsp; | &nbsp;Privacy Policy</span>
</div>
</body>
</html>
```